Conference program advertisement

Our business www.clinic ledgerwise.com.au is a good sponsor of the conference program run by the Pacific Rim Guild of Perioperative Medicine (PRGPM) here in Western Australia.
We have been running the same ad for a while and so we could do with a fresh new presence.
We have a conference banner and other signage that we'll use at the trade show so we're not looking to rebrand. Just looking for a new ad.
Specification is full colour A4, high res PDF
(Because I'm using my phone to create this job, I cannot seem to upload the existing ad. I'll do do ASAP.)

Target Market(s)

Specialist doctors

Industry/Entity Type

Trade

Font styles to use
Sans Serif

Colors

Designer to choose colors to be used in the design.

Requirements
Must have
• A4
Existing logo and colour scheme

```html
<!DOCTYPE html>
<html lang="en">
<head>
<meta charset="utf-8">
<title>Clinic Ledgerwise – Advertisement</title>
<link href="https://fonts.googleapis.com/css2?family=Oswald:wght@400&family=Open+Sans:wght@600;700&display=swap" rel="stylesheet">
<style>
  :root {
    --brand-red: #b5202e;
    --ink: #1d1d1f;
    --band-grey: #dcdfe6;
    --panel-teal: #5fb6cd;
    --panel-deep: #3e9ab4;
    --footer-dark: #1c1416;
    --footer-text: #e8e8e8;
    --footer-link: #7fd0e4;
    --mark-grey: #c4c4c4;
  }
  * { margin: 0; padding: 0; box-sizing: border-box; }
  html, body { width: 848px; height: 1200px; overflow: hidden; background: #ffffff; }
  .ad {
    position: relative;
    width: 848px;
    height: 1200px;
    background: #ffffff;
    font-family: "Open Sans", Verdana, sans-serif;
    color: var(--ink);
  }

  /* Brand block */
  .brand {
    position: absolute;
    top: 0;
    left: 0;
    width: 848px;
    height: 318px;
    display: flex;
    align-items: center;
    justify-content: center;
    gap: 24px;
  }
  .brand-square {
    width: 120px;
    height: 120px;
    border-radius: 12px;
    background: var(--mark-grey);
  }
  .brand-name {
    font-family: "Open Sans", Verdana, sans-serif;
    font-weight: 700;
    font-size: 34px;
    line-height: 40px;
    color: var(--ink);
  }

  /* Intro band */
  .intro {
    position: absolute;
    top: 318px;
    left: 0;
    width: 848px;
    height: 332px;
    background: var(--band-grey);
    padding: 46px 62px 0 72px;
  }
  .headline {
    font-family: "Oswald", "Arial Narrow", sans-serif;
    font-weight: 400;
    font-size: 60px;
    line-height: 63px;
    color: var(--ink);
    letter-spacing: -0.5px;
  }
  .headline .accent { color: var(--brand-red); }
  .intro-copy {
    margin-top: 12px;
    font-size: 14.4px;
    line-height: 17.6px;
    font-weight: 600;
    letter-spacing: 0.3px;
    color: var(--ink);
  }

  /* Services and photo */
  .services {
    position: absolute;
    top: 650px;
    left: 0;
    width: 848px;
    height: 405px;
  }
  .service-list {
    position: absolute;
    left: 0;
    top: 0;
    width: 356px;
    height: 405px;
    background: linear-gradient(180deg, var(--panel-teal), var(--panel-deep));
    list-style: none;
    padding-top: 22px;
  }
  .service-list li {
    position: relative;
    padding: 5px 56px 5px 88px;
    font-size: 12px;
    line-height: 15px;
    font-weight: 700;
    letter-spacing: 0.6px;
    text-transform: uppercase;
    color: #ffffff;
    border-bottom: 1px solid rgba(255,255,255,0.35);
  }
  .service-list li:nth-child(odd) { background: rgba(255,255,255,0.14); }
  .service-list li::before {
    content: "";
    position: absolute;
    left: 73px;
    top: 11px;
    width: 4px;
    height: 4px;
    border-radius: 50%;
    background: #ffffff;
  }
  .service-photo {
    position: absolute;
    left: 356px;
    top: 0;
    width: 492px;
    height: 405px;
    background: linear-gradient(135deg, #eef3f6 0%, #c9dde6 40%, #5fb3c8 75%, #3f8fa6 100%);
  }

  /* Footer */
  .contact {
    position: absolute;
    top: 1055px;
    left: 0;
    width: 848px;
    height: 145px;
    background: var(--footer-dark);
    color: var(--footer-text);
    font-size: 10.6px;
    line-height: 15px;
    font-weight: 600;
  }
  .contact-left { position: absolute; left: 74px; top: 52px; }
  .contact-right { position: absolute; right: 70px; top: 45px; text-align: right; }
  .contact-web { color: var(--footer-link); font-size: 15px; line-height: 20px; font-weight: 600; }
</style>
</head>
<body>
<main class="ad">
  <header class="brand">
    <div class="brand-square"></div>
    <span class="brand-name">Clinic Ledgerwise</span>
  </header>

  <section class="intro">
    <h1 class="headline">IS ADMINISTRATION EATING<br>UP <span class="accent">YOUR VALUABLE TIME</span>?</h1>
    <p class="intro-copy">Admin can consume a large amount of time for doctors working in private practice. From generating accounts to chasing up bad debts, from sitting on holdwith health funds, or trawling through remittance advices to getting accreditation papers and submitting provider number applications properly – we’re sure you would prefer to focus on being a doctor rather than worrying about paperwork and piles of admin. Clinic Ledgerwise is here to help – contact us today if you’re ready to remove the burden of admin.</p>
  </section>

  <section class="services">
    <ul class="service-list">
      <li>Private billing</li>
      <li>VMP billing</li>
      <li>Practice management</li>
      <li>Organise lists</li>
      <li>Cover lists</li>
      <li>Banking</li>
      <li>Public scheme and health fund registrations</li>
      <li>Fee estimates and informed financial consent</li>
      <li>Bill pay and credit card payments</li>
      <li>Electronic claiming to health funds</li>
      <li>GST reporting</li>
      <li>Hospital accreditations</li>
    </ul>
    <div class="service-photo" role="img" aria-label="Photo of a surgeon in teal scrubs working on a laptop in a bright hospital, with colleagues blurred in the background"></div>
  </section>

  <footer class="contact">
    <div class="contact-left">
      Rowan Castell Mobile +61 400 555 182<br>
      Office 08 5550 1427 • Fax 08 5550 1490<br>
      Level 2, Suite 12, 450 Marlow Terrace, Harbourview, WA, 6990
    </div>
    <div class="contact-right">
      PO Box 318, Harbourview WA 6990<br>
      rowan@clinicledgerwise.com.au<br>
      <span class="contact-web">www.clinicledgerwise.com.au</span>
    </div>
  </footer>
</main>
</body>
</html>
```